Current website re-design to a updated look and feel.

We currently have a website www.brightlanefreight.com that we want to give an updated look and feel to. We are a logistics company that competes with Harbex, Dm Whitfield, Tarn but on a smaller scale. We want something fresh and updated. We have two locations one in downtown Harlow, IL and one in Palatine IL. We are a fun group that also gets the job done. We know we need pictures of both locations and possibly a video, but we need fresh design ideas. The 'who we are' page is really the only page that we currently want to keep. The 'what we do' page needs to be completely re-done from a look and feel for sure.

Target Market(s)

Anyone who uses Truck transportation to move their product. Mainly US manufacturers.

Industry/Entity Type

Logistics

Number of Pages Required

5+ page

Font styles to use
Sans Serif

Colors
5c91c4
0355a3
d0dfed

Requirements
Must have
• The new design must entice people to want to do business with us. The design must have locations for pictures and at least one video which we know we will have to provide. Design must be easy to navigate.

```html
<!DOCTYPE html>
<html lang="en">
<head>
<meta charset="utf-8">
<title>Brightlane Freight</title>
<link href="https://fonts.googleapis.com/css2?family=Lato:wght@300;400;700;900&family=Cinzel:wght@400;500&family=Crimson+Text:wght@400&family=Roboto:wght@400;500&display=swap" rel="stylesheet">
<style>
:root{
  --navy:#0b2c9c;
  --cyan:#0a93cb;
  --link:#2aa9e2;
  --red:#b5282e;
  --ink:#1a1a1a;
  --grey:#6b6b6b;
  --white:#ffffff;
}
*{margin:0;padding:0;box-sizing:border-box}
html,body{width:774px;height:1200px;overflow:hidden}
body{position:relative;font-family:"Roboto",Arial,sans-serif;color:var(--ink)}
.backdrop{position:absolute;inset:0;background:linear-gradient(180deg,#2c3b55 0%,#5c7190 22%,#b0a684 48%,#8a6f3a 62%,#3a3630 80%,#1f1f21 100%)}
.page{position:absolute;left:50px;top:50px;width:675px;height:1099px;background:linear-gradient(180deg,#eef0f2 0%,#e2e5e8 45%,#d9dcde 100%);box-shadow:0 0 8px rgba(0,0,0,.35)}
.abs{position:absolute}
/* header */
.brand{left:10px;top:18px;display:flex;align-items:center;gap:8px}
.brand-name{font-family:"Lato",sans-serif;font-weight:400;font-size:32px;color:var(--navy);letter-spacing:-1px}
.brand-tag{font-family:"Lato",sans-serif;font-weight:700;font-size:7px;line-height:8px;color:var(--navy)}
.call{right:12px;top:22px;display:flex;gap:8px;align-items:center}
.call-label{font-family:"Lato",sans-serif;font-size:9.5px;color:#333}
.call-num{font-family:"Lato",sans-serif;font-weight:300;font-size:14px;color:var(--red);letter-spacing:.3px}
/* nav */
.nav{left:0;top:77px;width:675px;height:33px;background:var(--navy)}
.nav a{font-family:"Lato",sans-serif;font-size:12.5px;color:var(--link);text-decoration:none;position:absolute;top:0;height:33px;line-height:33px}
.nav a.active{background:var(--cyan);color:var(--white);padding:0 15px;left:45px}
/* hero */
.hero{left:8px;top:118px;width:659px;height:304px;background:linear-gradient(180deg,#cfe2f3 0%,#a9cbe6 45%,#6fa6cf 62%,#3f7fb3 100%);box-shadow:0 2px 5px rgba(0,0,0,.3)}
.hero-ship{position:absolute;right:0;top:20px;width:360px;height:230px;background:linear-gradient(160deg,#9fb7c9 0%,#b65a3d 45%,#f1b21f 75%,#f3c24a 100%);opacity:.85;border-radius:4px 0 0 4px}
.hero-title{position:absolute;left:21px;top:84px;font-family:"Lato",sans-serif;font-weight:900;color:#111;line-height:1}
.hero-title .l1{font-size:40px;display:block;letter-spacing:-1px}
.hero-title .l2{font-size:27px;display:block;margin-top:6px;letter-spacing:-.5px}
.hero-copy{position:absolute;left:21px;top:158px;width:260px;font-size:12.5px;line-height:16px;color:#111}
.arrow{position:absolute;top:229px;width:29px;height:29px;border-radius:50%;background:var(--white);display:flex;align-items:center;justify-content:center}
/* services */
.section-title{left:0;width:675px;top:455px;text-align:center;font-family:"Cinzel",serif;font-size:25px;color:#111}
.card{top:491px;width:161px}
.card-img{width:161px;height:94px}
.card-title{margin-top:24px;text-align:center;font-family:"Crimson Text",serif;font-size:13px;color:var(--navy)}
.card-copy{margin-top:4px;text-align:center;font-size:9.6px;line-height:13.5px;color:var(--grey);padding:0 6px}
.btn{display:flex;align-items:center;justify-content:center;gap:3px;height:29px;width:114px;border-radius:15px;font-size:12.5px;border:1.5px solid var(--navy);color:var(--navy);background:transparent;margin:13px auto 0}
.btn.solid{background:var(--navy);color:var(--white);box-shadow:0 2px 3px rgba(0,0,0,.3)}
/* about */
.about-name{left:16px;top:752px;font-family:"Lato",sans-serif;font-size:38px;color:var(--navy);letter-spacing:-1px}
.about-copy{left:16px;top:818px;width:350px;font-size:10px;line-height:13.6px;color:#555}
.about-btn{left:16px;top:900px;width:122px;height:33px;border-radius:17px;margin:0}
/* contact */
.touch{left:398px;top:732px;width:268px;height:201px;background:var(--cyan)}
.touch h2{font-family:"Cinzel",serif;font-weight:400;font-size:24px;color:var(--white);text-align:center;margin-top:18px}
.touch p{font-size:9.5px;color:#d8eef8;text-align:center;margin-top:6px}
.field{position:absolute;border:1px solid #d8f0fa;font-size:9.5px;color:var(--white);padding:6px 8px}
.submit{left:476px;top:917px;width:120px;height:33px;border-radius:17px;background:var(--white);border:1.5px solid var(--cyan);color:var(--navy);font-size:12.5px;display:flex;align-items:center;justify-content:center}
/* footer */
.footer{left:0;top:984px;width:675px;height:115px;background:var(--navy)}
.foot-link{position:absolute;top:24px;font-size:10px;color:var(--white)}
.foot-link.active{color:var(--link);text-decoration:underline}
.social{position:absolute;top:11px;width:25px;height:25px;border-radius:50%;border:1.5px solid var(--white)}
.social.on{background:var(--white);width:30px;height:30px;top:9px}
.rule{position:absolute;left:22px;top:49px;width:629px;height:1px;background:rgba(255,255,255,.35)}
.addr{position:absolute;left:48px;top:70px;font-family:"Crimson Text",serif;font-size:12.5px;line-height:17px;color:var(--white)}
.phones{position:absolute;left:202px;top:70px;font-size:10px;line-height:15px;color:var(--white)}
.mail{position:absolute;left:337px;top:78px;font-size:10px;color:var(--white)}
.copy{position:absolute;right:25px;top:66px;text-align:right;font-size:9.5px;line-height:15px;color:var(--white)}
.copy span{color:var(--link)}
</style>
</head>
<body>
<div class="backdrop" role="img" aria-label="Open road under a dramatic cloudy sky at sunset"></div>

<main class="page">
  <header>
    <div class="abs brand">
      <span class="brand-name">Brightlane</span>
      <span class="brand-tag">Transportation,<br>Distribution &amp;<br>Warehousing Inc.</span>
    </div>
    <div class="abs call">
      <svg width="26" height="26" viewBox="0 0 24 24" aria-hidden="true"><path d="M6.6 10.8a15 15 0 0 0 6.6 6.6l2.2-2.2c.3-.3.7-.4 1-.2 1.1.4 2.3.6 3.6.6.6 0 1 .4 1 1V20c0 .6-.4 1-1 1A17 17 0 0 1 3 4c0-.6.4-1 1-1h3.5c.6 0 1 .4 1 1 0 1.3.2 2.5.6 3.6.1.3 0 .7-.2 1z" fill="#111"/><path d="M14 3a7 7 0 0 1 7 7M14 6a4 4 0 0 1 4 4" stroke="#111" stroke-width="1.6" fill="none"/></svg>
      <div>
        <div class="call-label">Call us Now</div>
        <div class="call-num">555.014.2200</div>
      </div>
    </div>
  </header>

  <nav class="abs nav">
    <a class="active">Home</a>
    <a style="left:137px">What We Do</a>
    <a style="left:244px">How We Do It</a>
    <a style="left:359px">Who We Are</a>
    <a style="left:466px">Tracking</a>
    <a style="left:555px">Contact Us</a>
  </nav>

  <section class="abs hero">
    <div class="hero-ship" role="img" aria-label="Cargo ship loaded with containers beside a port crane"></div>
    <h1 class="hero-title"><span class="l1">RELEX.</span><span class="l2">WE GOT THIS.</span></h1>
    <p class="hero-copy">We provide friendly, exceptional service that makes it easy to do business with us. Give us a call today !</p>
    <div class="arrow" style="left:27px"><svg width="10" height="12" viewBox="0 0 10 12"><path d="M7 1 2 6l5 5" stroke="#f07a1e" stroke-width="1.6" fill="none"/></svg></div>
    <div class="arrow" style="left:61px"><svg width="10" height="12" viewBox="0 0 10 12"><path d="M3 1l5 5-5 5" stroke="#f07a1e" stroke-width="1.6" fill="none"/></svg></div>
  </section>

  <h2 class="abs section-title">WHAT WE DO</h2>

  <article class="abs card" style="left:11px">
    <div class="card-img" role="img" aria-label="Container ship sailing past a city skyline" style="background:linear-gradient(180deg,#b9d8ea,#3f8db8)"></div>
    <h3 class="card-title">Freight Management</h3>
    <p class="card-copy">We strive for a perfect delivery and promise to be there for anything you may need...</p>
    <a class="btn solid">READ MORE <b>»</b></a>
  </article>
  <article class="abs card" style="left:176px">
    <div class="card-img" role="img" aria-label="Row of colourful trucks parked at sunset" style="background:linear-gradient(180deg,#f0a23a,#7d8a99 60%,#c9c3b6)"></div>
    <h3 class="card-title">Product Transportation</h3>
    <p class="card-copy">We strive for a perfect delivery and promise to be there for anything you may need...</p>
    <a class="btn">READ MORE <b>»</b></a>
  </article>
  <article class="abs card" style="left:342px">
    <div class="card-img" role="img" aria-label="Warehouse aisle stacked with cardboard boxes" style="background:linear-gradient(180deg,#d8c9ad,#9b7a52)"></div>
    <h3 class="card-title">Warehouse &amp; Distribution</h3>
    <p class="card-copy">We strive for a perfect delivery and promise to be there for anything you may need...</p>
    <a class="btn">READ MORE <b>»</b></a>
  </article>
  <article class="abs card" style="left:507px">
    <div class="card-img" role="img" aria-label="Semi truck driving on a highway through green fields" style="background:linear-gradient(180deg,#4f8fd1,#b7d3ec 55%,#6f9a3c)"></div>
    <h3 class="card-title">Carriers</h3>
    <p class="card-copy">We strive for a perfect delivery and promise to be there for anything you may need...</p>
    <a class="btn">READ MORE <b>»</b></a>
  </article>

  <div class="abs about-name">Brightlane</div>
  <p class="abs about-copy">Brightlane Freight welcomes you to our growing family of clients! We have over 26 years of experience in helping people solve their logistics needs from coast-to-coast. We also provide friendly, exceptional service that makes it easy to do business with us. Give us a call today and experience the difference for yourself!</p>
  <a class="abs btn solid about-btn">READ MORE <b>»</b></a>

  <form class="abs touch">
    <h2>GET IN TOUCH</h2>
    <p>Lorem Ipsum is simply dummy text of the printing.</p>
    <div class="field" style="left:16px;top:74px;width:118px;height:27px">Name</div>
    <div class="field" style="left:138px;top:74px;width:117px;height:27px">Contact No.</div>
    <div class="field" style="left:16px;top:104px;width:239px;height:27px">E mail ID</div>
    <div class="field" style="left:16px;top:135px;width:239px;height:43px">Message...</div>
  </form>
  <div class="abs submit">SUBMIT</div>

  <footer class="abs footer">
    <a class="foot-link active" style="left:25px">Home</a>
    <a class="foot-link" style="left:72px">About</a>
    <a class="foot-link" style="left:118px">Srevices</a>
    <a class="foot-link" style="left:173px">Process</a>
    <a class="foot-link" style="left:227px">Track</a>
    <a class="foot-link" style="left:274px">Contact Us</a>
    <span class="social on" style="left:512px" aria-label="Social link"></span>
    <span class="social" style="left:546px" aria-label="Social link"></span>
    <span class="social" style="left:576px" aria-label="Social link"></span>
    <span class="social" style="left:606px" aria-label="Social link"></span>
    <div class="rule"></div>

    <svg class="abs" style="left:23px;top:72px" width="14" height="22" viewBox="0 0 14 22"><path d="M7 0a7 7 0 0 0-7 7c0 5 7 15 7 15s7-10 7-15a7 7 0 0 0-7-7z" fill="#fff"/><circle cx="7" cy="7" r="2.6" fill="#0b2c9c"/></svg>
    <div class="addr">downtown Harlow, IL<br>Fenwick, IL</div>

    <svg class="abs" style="left:176px;top:72px" width="22" height="22" viewBox="0 0 24 24"><path d="M6.6 10.8a15 15 0 0 0 6.6 6.6l2.2-2.2c.3-.3.7-.4 1-.2 1.1.4 2.3.6 3.6.6.6 0 1 .4 1 1V20c0 .6-.4 1-1 1A17 17 0 0 1 3 4c0-.6.4-1 1-1h3.5c.6 0 1 .4 1 1 0 1.3.2 2.5.6 3.6.1.3 0 .7-.2 1z" fill="#fff"/></svg>
    <div class="phones">555.014.2200<br>555.014.2202</div>

    <svg class="abs" style="left:310px;top:78px" width="24" height="17" viewBox="0 0 24 17"><rect x="0.5" y="0.5" width="23" height="16" rx="1.5" fill="#fff"/><path d="M1 1l11 9 11-9" stroke="#0b2c9c" stroke-width="1.4" fill="none"/></svg>
    <div class="mail">info@brightlanefreight.com</div>

    <div class="copy">© 2017 <span>Brightlane Freight.</span><br>All rights reserved.</div>
  </footer>
</main>
</body>
</html>
```